Brochure Design Project for Q7

We are needing a brochure for our new company, Q7. We are based out of Columbus, Ohio. We are providing security for schools. We will be hiring veterans and former police officers to monitor schools and protect the children and staff.

Q7 Vision Statement:

To enable a safe and secure learning environment that will ensure prosperity and
possibility that our children deserve and with the parents peace of mind.

Q7 Mission Statement:

To empower our children and teachers by providing the world’s foremost security
professionals to preserve the learning environment from grades K-12. Q7 will actively
seek seasoned qualified security professionals to protect our children and teachers. We
will vet, train, deploy and manage our security professionals. We will strive to become the employer of choice for Security Professionals.

We would like our logo on the brochure with the following contact information:

phone number: 614-555-0192
email: mikeharwell#q7guarding.example
(not sure of the website yet, I will send that to you when I get it)
address: P.O. Box 815, Larkfield Ohio 43990

We have established our website address and it is:  Q7guarding.example

We would like to have this on the flyer.

Our new email is:  mikeharwell#q7guarding.example
 
Could you please make these changes today because we have a mail out tomorrow.

```html
<!DOCTYPE html>
<html lang="en">
<head>
<meta charset="utf-8">
<title>Q7 School Security Brochure</title>
<link rel="stylesheet" href="https://fonts.googleapis.com/css2?family=Exo+2:wght@700;800&family=Titillium+Web:wght@400;600&display=swap">
<style>
  :root {
    --page-bg: #ffffff;
    --navy: #1b2670;
    --navy-deep: #0a1142;
    --navy-mid: #25318a;
    --gold: #d2ad55;
    --gold-soft: #b89347;
    --white: #ffffff;
    --body-text: #c9cfee;
    --silver-hi: #f2f3f6;
    --silver-lo: #8e93a3;
    --ghost-text: rgba(255,255,255,0.04);
  }
  * { margin: 0; padding: 0; box-sizing: border-box; }
  html, body { width: 1200px; height: 577px; overflow: hidden; background: var(--page-bg); }
  .canvas { position: relative; width: 1200px; height: 577px; }

  .spread { position: absolute; top: 48px; display: flex; box-shadow: 0 18px 28px -18px rgba(0,0,0,0.55); }
  .spread--exterior { left: 30px; }
  .spread--interior { left: 630px; }

  .panel {
    position: relative; width: 270px; height: 480px; overflow: hidden;
    background: radial-gradient(ellipse at 70% 75%, var(--navy-mid) 0%, var(--navy) 45%, var(--navy-deep) 100%);
    font-family: "Titillium Web", sans-serif; color: var(--white);
  }

  .silver-band { position: absolute; left: 0; width: 100%; height: 7px;
    background: linear-gradient(180deg, var(--silver-hi), var(--silver-lo)); }

  .photo { position: absolute; left: 0; width: 100%; }
  .photo--chalkboard { top: 92px; height: 196px;
    background: linear-gradient(180deg, #5d7a6c 0%, #6f8c7c 55%, #8a7a66 100%); }
  .photo--classroom { top: 92px; height: 196px;
    background: linear-gradient(180deg, #4d7a5e 0%, #c8b8a0 55%, #b9a58b 100%); }

  .brand-mark { position: absolute; display: flex; align-items: center; gap: 6px;
    font-family: "Exo 2", sans-serif; font-weight: 800; color: var(--gold); line-height: 1; }
  .brand-mark__square { border: 2px solid var(--gold); }
  .brand-mark--large { top: 34px; right: 22px; font-size: 40px; }
  .brand-mark--large .brand-mark__square { width: 14px; height: 14px; }
  .brand-mark--small { left: 90px; top: 346px; font-size: 22px; }
  .brand-mark--small .brand-mark__square { width: 9px; height: 9px; }

  .headline { position: absolute; left: 34px; font-family: "Exo 2", sans-serif; font-weight: 800;
    text-transform: uppercase; line-height: 0.98; letter-spacing: -0.3px; }
  .headline--front { top: 318px; font-size: 29px; }
  .headline--left { top: 316px; font-size: 27px; left: 38px; }
  .headline .gold { color: var(--gold); }

  .tagline { position: absolute; left: 34px; font-size: 6.5px; font-weight: 600; letter-spacing: 1.3px; text-transform: uppercase; }
  .tagline--front { top: 442px; }
  .tagline--left { top: 435px; left: 38px; }
  .tagline .gold { color: var(--gold); }

  .ghost-words { position: absolute; top: 22px; left: 10px; font-family: "Exo 2", sans-serif; font-weight: 800;
    font-size: 29px; line-height: 0.98; text-transform: uppercase; color: var(--ghost-text); }

  .contact-list { position: absolute; left: 90px; top: 378px; list-style: none; font-size: 6.6px; line-height: 1.55; color: var(--body-text); white-space: nowrap; }
  .contact-list b { color: var(--gold-soft); font-weight: 400; margin-right: 3px; }

  .statement { position: absolute; left: 40px; right: 26px; }
  .statement--vision { top: 162px; }
  .statement--mission { top: 258px; }
  .statement__title { font-family: "Exo 2", sans-serif; font-weight: 800; font-size: 26px; line-height: 1; text-transform: uppercase; margin-bottom: 3px; }
  .statement__title .gold { color: var(--gold); }
  .statement p { font-size: 8.3px; line-height: 1.32; color: var(--body-text); margin-bottom: 8px; }
</style>
</head>
<body>
<main class="canvas">

  <section class="spread spread--exterior" aria-label="Exterior spread">
    <article class="panel panel--back" aria-label="Back cover">
      <div class="ghost-words" aria-hidden="true">We will<br>protect<br>your little<br>genius<br>We will<br>protect<br>your little<br>genius<br>We will<br>protect<br>your little<br>genius</div>
      <div class="brand-mark brand-mark--small"><span class="brand-mark__square"></span>Q7</div>
      <ul class="contact-list">
        <li><b>[address]</b>P.O. Box 815, Larkfield Ohio 43990</li>
        <li><b>[phone]</b>614-555-0192</li>
        <li><b>[email]</b>mikeharwell#q7guarding.example</li>
        <li><b>[website]</b>www.q7guarding.example</li>
      </ul>
    </article>

    <article class="panel panel--front" aria-label="Front cover">
      <div class="silver-band" style="top:86px"></div>
      <div class="photo photo--chalkboard" role="img" aria-label="Photo of a child in a wild grey wig, arms crossed, in front of a chalkboard full of equations"></div>
      <div class="silver-band" style="top:288px"></div>
      <div class="brand-mark brand-mark--large"><span class="brand-mark__square"></span>Q7</div>
      <h1 class="headline headline--front">“We will<br><span class="gold">protect</span><br>your little<br><span class="gold">genius”</span></h1>
      <p class="tagline tagline--front"><span class="gold">Security</span> where you need it the most</p>
    </article>
  </section>

  <section class="spread spread--interior" aria-label="Interior spread">
    <article class="panel panel--left" aria-label="Inside left">
      <div class="silver-band" style="top:86px"></div>
      <div class="photo photo--classroom" role="img" aria-label="Photo of a classroom with pupils raising their hands towards the teacher"></div>
      <div class="silver-band" style="top:288px"></div>
      <h2 class="headline headline--left">“At school<br><span class="gold">they need</span><br>to feel<br><span class="gold">secure”</span></h2>
      <p class="tagline tagline--left"><span class="gold">Security</span> where you need it the most</p>
    </article>

    <article class="panel panel--right" aria-label="Inside right">
      <div class="silver-band" style="top:86px"></div>
      <div class="brand-mark brand-mark--large"><span class="brand-mark__square"></span>Q7</div>
      <div class="statement statement--vision">
        <h3 class="statement__title">Q7 <span class="gold">Vision</span></h3>
        <p>To enable a safe and secure learning environment that will ensure prosperity and possibility that our children deserve and with the parents peace of mind.</p>
      </div>
      <div class="statement statement--mission">
        <h3 class="statement__title">Q7 <span class="gold">Mission</span></h3>
        <p>To empower our children and teachers by providing the world’s foremost security professionals to preserve the learning environment from grades K-12.</p>
        <p>Q7 will actively seek seasoned qualified security professionals to protect our children and teachers.</p>
        <p>We will vet, train, deploy and manage our security professionals.<br>We will strive to become the employer of choice for Security Professionals.</p>
      </div>
    </article>
  </section>

</main>
</body>
</html>
```